Book jacket for Drumlore

We need a book jacket design (hard cover front, back, spine, flaps; soft cover and eBook). for a social psychology book with the general cluelessness (being "out of it") of how people function both in their personal and social lives. This is the third book written by the author, a practicing psychiatrist, and the content centers on a single subject, people's lack of genuine emotional contact, their cluelessness with themselves and with current national and world events.

Target Market(s)

People who want to better understand the state the nation and world is in now, and what they can do about it.

Font styles to use
Serif
Sans Serif

Requirements
Must have
• Bold, eye-catching cover
Nice to have
• Like the idea of separating the title word (drum lore) to better emphasize the concept of lack of contact

```html
<!DOCTYPE html>
<html lang="en">
<head>
<meta charset="utf-8">
<title>Drumlore — Book Jacket Front</title>
<link href="https://fonts.googleapis.com/css2?family=Oswald:wght@400;700&display=swap" rel="stylesheet">
<style>
  :root {
    --backdrop: #484848;
    --paper: #ffffff;
    --stamp-blue: #22649c;
    --ink: #111111;
  }
  * { margin: 0; padding: 0; box-sizing: border-box; }
  html, body {
    width: 1200px;
    height: 1135px;
    overflow: hidden;
    background: var(--backdrop);
  }
  .cover {
    position: absolute;
    left: 228px;
    top: 71px;
    width: 670px;
    height: 956px;
    background: var(--paper);
    overflow: hidden;
  }
  .title-stamp {
    position: absolute;
    left: 0;
    top: 0;
    width: 670px;
    height: 956px;
  }
  .stamp-band { fill: var(--stamp-blue); }
  .book-title {
    font-family: "Oswald", "Arial Narrow", sans-serif;
    font-weight: 700;
    font-size: 167px;
    fill: var(--stamp-blue);
  }
  .author-name {
    position: absolute;
    left: 0;
    width: 100%;
    top: 804px;
    font-family: "Oswald", "Arial Narrow", sans-serif;
    font-weight: 400;
    font-size: 51px;
    line-height: 1;
    letter-spacing: 5px;
    color: var(--ink);
    text-align: center;
    text-transform: uppercase;
  }
</style>
</head>
<body>
  <main class="cover">
    <svg class="title-stamp" viewBox="0 0 670 956" role="img" aria-label="Drumlore">
      <g transform="rotate(-4.86 335 420)">
        <rect class="stamp-band" x="-20" y="302" width="672" height="24"/>
        <text class="book-title" x="331" y="482" text-anchor="middle" textLength="541" lengthAdjust="spacingAndGlyphs">DRUMLORE</text>
        <rect class="stamp-band" x="14" y="501" width="680" height="24"/>
      </g>
    </svg>
    <p class="author-name">Martin Avery M.D.</p>
  </main>
</body>
</html>
```